Flaschenetiketten-Design in rechteckiger Grundform für Biermanufaktur
Der Kontakt war sehr professionell und angenehm. Wir wurden hilfreich beraten. Auf unser Feedback haben wir in kurzer Zeit jeweils neue Entwürfe erhalten. Die Zusammenarbeit und der Service war deutlich über unseren Vorstellungen. Wir können KorvaneDeck nur weiterempfehlen!
Zielgruppe
Wir repräsentieren eine Bier-Manufaktur in der Gründungsphase und sind auf der Suche nach einem Designvorschlag für die Flaschenetiketten.
Unsere Zielgruppe sind Liebhaber, die auf der Suche nach dem Speziellen und Lokalen sind. Der Biergenuss abseits des Massenmarktes soll im Entwurf sichtbar/transportiert werden. Die Bier-Manufaktur steht zeitgleich für Trend-Kreationen mit bodenständigem Ursprung.
Aufgabenstellung
Die Herkunft der Gründer Familie aus dem Schweizer Kanton Simplon soll im Vordergrund stehen, hierzu bitte das Familienwappen / einzelne Elemente siehe Dateiupload berücksichtigen.
Das Etikett soll eine rechteckige Grundform haben.
Folgende Angaben sollen sich im Etikett wiederfinden:
- Biersorte: 'Lager' (zukünftig soll es möglich sein, Biersorte auf dem Etikett zu wechseln)
Brand: 'Mostly Grafun'
'Biermanufaktur Walliser Ursprungs'
Die Schrift soll klar und nicht zu verspielt sein.

```html
<!DOCTYPE html>
<html lang="de">
<head>
<meta charset="utf-8">
<title>Mostly Grafun – Etikettenreihe</title>
<link rel="stylesheet" href="https://fonts.googleapis.com/css2?family=Oswald:wght@600&family=PT+Sans+Narrow&family=Roboto+Condensed:wght@700&display=swap">
<style>
  :root {
    --bg: #ececec;
    --royal: #1b4f9c;
    --royal-deep: #123a78;
    --sky: #3f8fd8;
    --sky-light: #67aee6;
    --black: #1c1c1c;
    --paper: #fbfbfb;
    --gold: #d9a834;
    --gold-light: #efcf6e;
    --red: #c42230;
    --white: #ffffff;
    --crest-blue: #2c62b0;
  }
  * { box-sizing: border-box; margin: 0; padding: 0; }
  html, body { width: 1200px; height: 724px; overflow: hidden; }
  body {
    background: var(--bg);
    position: relative;
    font-family: "PT Sans Narrow", sans-serif;
  }
  .label-set {
    position: absolute;
    top: 0;
    width: 200px;
    height: 724px;
    margin-left: -100px;
  }
  .set-blue { left: 368px; }
  .set-black { left: 603px; }
  .set-white { left: 829px; }

  .neck-label {
    position: absolute;
    top: 126px;
    left: 38px;
    width: 124px;
    height: 96px;
    display: flex;
    align-items: center;
    justify-content: center;
    border-top: 4px solid var(--gold);
    border-bottom: 4px solid var(--gold);
  }
  .body-label {
    position: absolute;
    top: 374px;
    left: 0;
    width: 200px;
    height: 244px;
    overflow: hidden;
    border-top: 4px solid var(--gold);
    border-bottom: 4px solid var(--gold);
    text-align: center;
  }
  .crest {
    width: 48px;
    height: 58px;
    border-radius: 4px 4px 24px 24px;
    background: linear-gradient(180deg, var(--crest-blue), var(--royal-deep));
    border: 3px solid var(--gold);
  }
  .crest-large {
    position: absolute;
    top: 22px;
    left: 76px;
    width: 48px;
    height: 56px;
    border-radius: 4px 4px 24px 24px;
  }
  .quality-mark {
    position: absolute;
    top: 10px;
    left: 0;
    width: 100%;
    font-family: "Roboto Condensed", sans-serif;
    font-size: 5px;
    line-height: 6px;
    letter-spacing: 0.5px;
    color: var(--white);
  }
  .brand-name {
    position: absolute;
    top: 88px;
    left: 0;
    width: 100%;
    font-family: "Oswald", sans-serif;
    font-weight: 600;
    font-size: 36px;
    line-height: 38px;
    text-transform: uppercase;
    letter-spacing: -0.5px;
    color: var(--white);
  }
  .origin-band {
    position: absolute;
    left: 0;
    bottom: 0;
    width: 100%;
    height: 54px;
    padding-top: 7px;
    font-size: 15px;
    line-height: 20px;
    color: var(--white);
  }

  /* blue variant */
  .set-blue .neck-label { background: var(--royal); }
  .set-blue .body-label { background: radial-gradient(ellipse at 50% 40%, var(--royal), var(--royal-deep)); }
  .set-blue .origin-band { background: linear-gradient(180deg, var(--sky), var(--sky-light)); }

  /* black variant */
  .set-black .neck-label { background: var(--black); border-color: var(--sky); }
  .set-black .body-label { background: var(--black); border-color: var(--sky); }
  .set-black .brand-name { text-transform: none; }
  .set-black .origin-band { background: linear-gradient(180deg, var(--sky), var(--royal)); }

  /* white variant */
  .set-white .neck-label { background: var(--paper); }
  .set-white .body-label { background: var(--paper); border-top: none; }
  .set-white .quality-mark { color: var(--black); }
  .set-white .crest-large { top: 20px; }
  .set-white .brand-name { color: var(--red); transform: rotate(-6deg); top: 82px; }
  .set-white .origin-band {
    background: linear-gradient(90deg, var(--gold), var(--gold-light), var(--gold));
    color: var(--black);
    transform: skewY(-8deg);
    transform-origin: left bottom;
    bottom: -10px;
    height: 56px;
    padding-top: 4px;
  }
  .set-white .origin-band span { display: block; transform: skewY(8deg); }
</style>
</head>
<body>
  <section class="label-set set-blue">
    <div class="neck-label"><div class="crest" role="img" aria-label="Familienwappen mit Sternen und Kreuz"></div></div>
    <div class="body-label">
      <p class="quality-mark">· PREMIUM QUALITÄT ·</p>
      <div class="crest crest-large" role="img" aria-label="Familienwappen mit Ährenkranz"></div>
      <h2 class="brand-name">Mostly<br>Grafun</h2>
      <p class="origin-band">Biermanufaktur Walliser<br>Ursprungs</p>
    </div>
  </section>

  <section class="label-set set-black">
    <div class="neck-label"><div class="crest" role="img" aria-label="Familienwappen mit Sternen und Kreuz"></div></div>
    <div class="body-label">
      <p class="quality-mark">· PREMIUM QUALITÄT ·</p>
      <div class="crest crest-large" role="img" aria-label="Familienwappen mit Ährenkranz"></div>
      <h2 class="brand-name">Mostly<br>Grafun</h2>
      <p class="origin-band">Biermanufaktur Walliser<br>Ursprungs</p>
    </div>
  </section>

  <section class="label-set set-white">
    <div class="neck-label"><div class="crest" role="img" aria-label="Familienwappen mit Sternen und Kreuz"></div></div>
    <div class="body-label">
      <p class="quality-mark">· PREMIUM QUALITÄT ·</p>
      <div class="crest crest-large" role="img" aria-label="Familienwappen mit goldenem Ährenkranz"></div>
      <h2 class="brand-name">Mostly<br>Grafun</h2>
      <p class="origin-band"><span>Biermanufaktur Walliser<br>Ursprungs</span></p>
    </div>
  </section>
</body>
</html>
```